We would like to create a flyer with our logo I have attached and would like you to add the NorthBrambleBID logo at the bottom.
I would like the flyer to have a urban vintage style to it.
Please add:
Email: Info@northbramblebid.co.uk
Twitter account: @Northbramblebid
Facebook account: The Copperline Vintage and Antique Market
Address: The Copperline, North Bramble, Q47 2XZ
Dates: Saturday 27 september 2014
Saturday 25 October 2014
Saturday 29 November 2014.
Please hight light the dates and the location.

Target Market(s)

Every one.

Font styles to use
Other font styles liked:
• Market Deco

Requirements
Must have
• My project should be eye catching.
• Dates and location should be clear.
• Please use this font: ‘Market Deco’
• Please source images which will suit the logo and style of layout.
Nice to have
• Colours which will contrast with the logo.
• Colour of logo is: purple is P95 -16c
• The layout on the word doc I like.

```html
<!DOCTYPE html>
<html lang="en">
<head>
<meta charset="utf-8">
<title>The Copperline Vintage and Antique Market</title>
<link rel="stylesheet" href="https://fonts.googleapis.com/css2?family=Righteous&family=Josefin+Sans:wght@600;700&display=swap">
<style>
  :root {
    --page-bg: #1c1c1c;
    --cream: #fff6e4;
    --ink: #2a1610;
    --plum: #3a2050;
    --plum-soft: #5b3a6e;
    --panel: rgba(255, 250, 240, 0.62);
    --band: rgba(214, 170, 90, 0.55);
    --band-edge: #5a3a1c;
  }
  * { box-sizing: border-box; margin: 0; padding: 0; }
  html, body {
    width: 998px; height: 1200px; overflow: hidden;
    background: var(--page-bg);
  }
  .flyer {
    position: absolute; left: 35px; top: 0;
    width: 928px; height: 1200px; overflow: hidden;
    font-family: "Josefin Sans", sans-serif;
    color: var(--ink);
  }
  .street-photo {
    position: absolute; inset: 0;
    background:
      radial-gradient(ellipse at 55% 55%, rgba(255,245,150,0.95) 0%, rgba(250,205,60,0.7) 30%, rgba(0,0,0,0) 60%),
      radial-gradient(ellipse at 70% 25%, rgba(240,190,90,0.6), rgba(0,0,0,0) 50%),
      linear-gradient(90deg, #8a1d14 0%, #c0561c 20%, #e8a831 45%, #f2c53e 60%, #c36a1c 85%, #7d1a12 100%);
  }
  .street-photo::after {
    content: ""; position: absolute; inset: 0;
    background: linear-gradient(180deg, rgba(120,30,10,0.35) 0%, rgba(0,0,0,0) 25%, rgba(0,0,0,0) 75%, rgba(120,20,10,0.45) 100%);
  }
  .centered { position: absolute; left: 0; width: 100%; text-align: center; }
  .title {
    font-family: "Righteous", sans-serif;
    font-size: 66px; line-height: 92px; top: 56px;
    color: var(--cream); letter-spacing: 2px; text-transform: uppercase;
    text-shadow: 3px 4px 0 #3a1a0c;
  }
  .welcome-band { position: absolute; left: 202px; top: 240px; width: 571px; height: 113px; }
  .welcome-text {
    font-family: "Righteous", sans-serif; font-size: 48px; letter-spacing: 4px;
    top: 272px; color: var(--ink);
  }
  .market-sign {
    position: absolute; left: 169px; top: 470px; width: 632px; height: 55px;
    background: var(--plum); border: 3px solid #c9b48a;
    display: flex; align-items: center; justify-content: center;
    font-family: "Righteous", sans-serif; font-size: 29px; color: var(--cream);
    letter-spacing: 1px; text-transform: uppercase;
  }
  .market-sign .amp { color: #d8a94a; margin: 0 14px; font-size: 36px; }
  .heading {
    font-family: "Righteous", sans-serif; font-size: 66px; line-height: 1;
    text-transform: uppercase; color: var(--ink);
  }
  .address-heading { top: 560px; }
  .address-line { top: 630px; font-size: 29px; font-weight: 700; text-transform: uppercase; }
  .dates-heading { top: 708px; }
  .date-row {
    font-size: 30px; font-weight: 700; text-transform: uppercase;
    display: flex; justify-content: center; align-items: center; gap: 6px;
  }
  .date-num {
    display: inline-flex; width: 38px; height: 38px; border-radius: 50%;
    background: var(--ink); color: var(--cream); font-size: 24px;
    align-items: center; justify-content: center; padding-top: 3px;
  }
  .date-1 { top: 785px; } .date-2 { top: 837px; } .date-3 { top: 888px; }
  .contact-panel {
    position: absolute; left: 69px; top: 951px; width: 793px; height: 143px;
    background: var(--panel); border-radius: 6px;
  }
  .contact-list { position: absolute; left: 42px; top: 8px; list-style: none; }
  .contact-list li {
    display: flex; align-items: center; gap: 12px; height: 42px;
    font-size: 16px; font-weight: 600; text-transform: uppercase; color: var(--plum);
  }
  .contact-icon {
    width: 36px; height: 36px; border-radius: 50%; background: var(--plum);
    display: flex; align-items: center; justify-content: center;
  }
  .brand {
    position: absolute; right: 20px; top: 22px; width: 200px; height: 100px;
    background: rgba(255,255,255,0.7); border-radius: 4px;
    display: flex; flex-direction: column; align-items: center; justify-content: center; gap: 8px;
  }
  .brand-mark { width: 30px; height: 30px; background: var(--plum-soft); }
  .brand-name { font-size: 19px; font-weight: 700; color: var(--plum-soft); }
  .website {
    top: 1118px; font-size: 29px; font-weight: 700; letter-spacing: 1px;
    color: var(--cream); text-transform: uppercase;
  }
</style>
</head>
<body>
<main class="flyer">
  <div class="street-photo" role="img" aria-label="Warm-toned street photograph of a shopping avenue with period buildings, overlaid with golden swirl flourishes"></div>

  <h1 class="centered title">The Copperline Vintage<br>and Antique Market</h1>

  <svg class="welcome-band" viewBox="0 0 571 113" aria-hidden="true">
    <path d="M20 20 Q285 -10 551 20 L541 95 Q285 68 30 95 Z" fill="var(--band)" stroke="var(--band-edge)" stroke-width="3"/>
  </svg>
  <p class="centered welcome-text">WELCOME</p>

  <div class="market-sign">Copperline Vintage <span class="amp">&amp;</span> Antique Market</div>

  <h2 class="centered heading address-heading">Address</h2>
  <p class="centered address-line">The Copperline, North Bramble, Q47 2XZ</p>

  <h2 class="centered heading dates-heading">Dates</h2>
  <p class="centered date-row date-1">Saturday <span class="date-num">27</span> September 2014</p>
  <p class="centered date-row date-2">Saturday <span class="date-num">25</span> October 2014</p>
  <p class="centered date-row date-3">Saturday <span class="date-num">29</span> November 2014</p>

  <section class="contact-panel">
    <ul class="contact-list">
      <li>
        <span class="contact-icon">
          <svg width="20" height="14" viewBox="0 0 20 14" aria-hidden="true">
            <rect x="1" y="1" width="18" height="12" fill="none" stroke="#fff6e4" stroke-width="1.8"/>
            <path d="M1 1 L10 8 L19 1" fill="none" stroke="#fff6e4" stroke-width="1.8"/>
          </svg>
        </span>
        Info@northbramblebid.co.uk
      </li>
      <li><span class="contact-icon"></span>@Northbramblebid</li>
      <li><span class="contact-icon"></span>The Copperline Vintage and Antique Market</li>
    </ul>
    <div class="brand">
      <span class="brand-mark"></span>
      <span class="brand-name">northbramblebid</span>
    </div>
  </section>

  <p class="centered website">www.northbramblebid.co.uk</p>
</main>
</body>
</html>
```